Business Card Design Project

We have 2 businesses which help each other.

Brightvale Care (providing nurses to hospitals/nursing homes etc)

and

Brightvale HR (providing nurses to our brightvale care business - but also providing workers for farms, restaurants meatworks etc)

We would like 2 separate business cards - but similar design and feel

Target Market(s)

Managers of nursing homes, hospitals, farms, meatworks, restauants

Industry/Entity Type

Business

Requirements
Must have
• both logos
https://www.filestashly.com/s/9k2m7q4tz1xw5np/BrightvaleHR-Logo-Horizontal.ai
https://www.filestashly.com/s/pe58vn2c0rj4kd/73192_518674_92817_sourcefile.ai

You may edit the layout of Brightvale HR logo

Name
position
mobile
Phone
name@brightvalehr.com.au
brigthvalehr.com.au

Name
position
mobile
phone
name@brightvalecare.net.au
brightvalecare.net.au

```html
<!DOCTYPE html>
<html lang="en">
<head>
<meta charset="utf-8">
<title>Brightvale HR – Business Card</title>
<link rel="stylesheet" href="https://fonts.googleapis.com/css2?family=Source+Sans+3:ital,wght@0,400;0,700;1,400&display=swap">
<style>
  :root {
    --navy: #1b4e9b;
    --sky: #27a9e1;
    --blue-deep: #0a79c0;
    --blue-light: #33bdee;
    --white: #ffffff;
    --shadow: #d3d6da;
    --badge: #c4c7cc;
  }
  html, body {
    margin: 0;
    padding: 0;
    overflow: hidden;
    background: var(--white);
  }
  .card {
    position: relative;
    width: 686px;
    height: 1200px;
    overflow: hidden;
    background: var(--white);
    font-family: "Source Sans 3", sans-serif;
  }
  .card-art {
    position: absolute;
    inset: 0;
  }
  .brand-mark {
    position: absolute;
    left: 46px;
    top: 229px;
    width: 132px;
    height: 132px;
    border-radius: 50%;
    background: var(--badge);
  }
  .brand-name {
    position: absolute;
    left: 200px;
    top: 276px;
    margin: 0;
    font-size: 64px;
    font-weight: 700;
    color: var(--navy);
    line-height: 1;
    letter-spacing: -0.5px;
    white-space: nowrap;
  }
  .tagline {
    position: absolute;
    right: 63px;
    top: 345px;
    margin: 0;
    font-size: 38px;
    line-height: 1;
    font-style: italic;
    color: var(--sky);
  }
  .person-name,
  .person-role {
    position: absolute;
    left: 0;
    width: 628px;
    margin: 0;
    text-align: center;
    color: var(--white);
    line-height: 1;
  }
  .person-name {
    top: 656px;
    font-size: 56px;
    font-weight: 700;
  }
  .person-role {
    top: 711px;
    font-size: 33px;
    font-weight: 400;
  }
  .contact {
    position: absolute;
    left: 48px;
    top: 833px;
    margin: 0;
    padding: 0;
    list-style: none;
    color: var(--white);
    font-size: 32px;
    line-height: 45px;
    white-space: nowrap;
  }
  .contact-label {
    display: inline-block;
    width: 127px;
  }
  .divider {
    position: absolute;
    left: 34px;
    top: 1047px;
    width: 601px;
    height: 4px;
    background: var(--white);
  }
  .website {
    position: absolute;
    left: 0;
    width: 622px;
    top: 1092px;
    margin: 0;
    text-align: center;
    color: var(--white);
    font-size: 44px;
    line-height: 1;
  }
</style>
</head>
<body>
<main class="card">
  <svg class="card-art" width="686" height="1200" viewBox="0 0 686 1200" aria-hidden="true">
    <defs>
      <linearGradient id="panel-gradient" x1="0" y1="0" x2="0" y2="1">
        <stop offset="0" stop-color="var(--blue-deep)"/>
        <stop offset="1" stop-color="var(--blue-light)"/>
      </linearGradient>
      <linearGradient id="top-gradient" x1="0" y1="0" x2="1" y2="0">
        <stop offset="0" stop-color="var(--blue-deep)"/>
        <stop offset="1" stop-color="var(--blue-light)"/>
      </linearGradient>
    </defs>
    <!-- top wave -->
    <path d="M0,0 H686 V72 Q380,262 0,108 Z" fill="var(--shadow)" opacity="0.55"/>
    <path d="M0,0 H686 V50 Q380,232 0,82 Z" fill="var(--white)"/>
    <path d="M0,0 H686 V25 Q380,175 0,52 Z" fill="url(#top-gradient)"/>
    <!-- lower panel -->
    <path d="M0,612 Q377,352 686,690 V1200 H0 Z" fill="var(--shadow)" opacity="0.55"/>
    <path d="M0,657 Q377,381 686,710 V1200 H0 Z" fill="url(#panel-gradient)"/>
  </svg>

  <span class="brand-mark"></span>
  <h1 class="brand-name">Brightvale HR</h1>
  <p class="tagline">tagline here</p>

  <h2 class="person-name">First Lastname</h2>
  <p class="person-role">executive of business cards</p>

  <ul class="contact">
    <li>first.lastname@brightvalehr.com.au</li>
    <li><span class="contact-label">mobile:</span>0491 570 318</li>
    <li><span class="contact-label">phone:</span>0491 570 642</li>
  </ul>

  <div class="divider"></div>
  <p class="website">brightvalehr.com.au</p>
</main>
</body>
</html>
```